QV Pathway Branding
Stationary - Business Card, Letter Head, Powerpoint file, Word Document, Email Signature.
QV Pathway Branding - Information Technology
Creative Brief
Professional
Darren M. L.
Founder
58 Ravel Pine Street #04-12 Orlan Plaza Singapore 142390
darrenm.l@qvpathway-example.com
www.qvpathway-example.com
BRN : 209874163K
The main idea of this contest is not just for the name card but a branding for our stationary. The following are the pointers/comments. I would like it if Icons were used Instead of Phone, Fax, Email, Web. Note: the 2 different Phone numbers in the Cell phone, each should have it's own line if possible. Please use white matte background. For additional effects on the namecard, you may use the different shades to create the effect. For Stationary, please ensure a word document format, powerpoint and email signature format is created as well as the other conventional document types. BRN is only required on the Letterheads. Extra type of formats for branding (e.g. Folder design) earns you extra Stars and ultimately seals the deal with creativity.
Please be creative in the design of the back of the business card. You are to freely manipulate the details given for back and front. Which means you may incorporate in the details in the design to be either the front and or the back.

```html
<!DOCTYPE html>
<html lang="en">
<head>
<meta charset="utf-8">
<title>QV Pathway Branding – Stationery Set</title>
<link href="https://fonts.googleapis.com/css2?family=Archivo:wght@400;700&display=swap" rel="stylesheet">
<style>
:root{
  --red:#e0262b;
  --ink:#2a2a2a;
  --grey:#8a8a8a;
  --rule:#c9c9c9;
  --paper:#ffffff;
  --black:#111111;
  --stage:#e6e4e1;
}
*{box-sizing:border-box;margin:0;padding:0}
html,body{width:1200px;height:878px;overflow:hidden;background:var(--stage)}
body{font-family:"Archivo",Arial,sans-serif;color:var(--ink)}
.canvas{position:relative;width:1200px;height:878px;overflow:hidden;background:var(--stage)}
.piece{position:absolute;background:var(--paper);box-shadow:0 3px 8px rgba(0,0,0,.25);overflow:hidden}
.band{position:absolute;left:0;right:0;background:var(--red)}
.hairline{position:absolute;left:0;right:0;height:1px;background:var(--rule)}

.logo{position:absolute;display:flex;align-items:center;gap:4px;white-space:nowrap}
.logo .logo-square{display:block;background:var(--red)}
.logo .logo-name{font-weight:700;color:var(--ink);letter-spacing:.02em;text-transform:uppercase}
.logo.sm .logo-square{width:7px;height:7px}.logo.sm .logo-name{font-size:11px}
.logo.md .logo-square{width:9px;height:9px}.logo.md .logo-name{font-size:15px}
.logo.on-dark .logo-name{color:#fff}
.tagline{position:absolute;font-size:5px;color:var(--grey);letter-spacing:.04em;white-space:nowrap}

.mark{position:absolute;display:flex;align-items:center;gap:6px;white-space:nowrap}
.mark .mark-square{display:block;background:var(--red)}
.mark .mark-name{font-weight:700;color:var(--red);text-transform:uppercase}
.mark.xl .mark-square{width:14px;height:14px}.mark.xl .mark-name{font-size:26px}
.mark.lg .mark-square{width:11px;height:11px}.mark.lg .mark-name{font-size:19px}
.mark.md .mark-square{width:7px;height:7px}.mark.md .mark-name{font-size:12px}

.small{position:absolute;font-size:5.5px;line-height:1.5;color:var(--ink);white-space:nowrap}
.web{position:absolute;font-size:6px;color:#fff;white-space:nowrap}
.contact-row{display:flex;align-items:center;gap:3px}
.ico{width:6px;height:6px;flex:none}

.folder-open{left:53px;top:67px;width:427px;height:360px;background:transparent;box-shadow:none}
.folder-open .sheet{position:absolute;inset:0}
.folder-back{left:504px;top:67px;width:216px;height:360px}

.card{width:216px;height:120px}
.card-front{left:739px;top:67px}
.card-back{left:739px;top:204px}
.card-mini{left:943px;top:583px;width:233px;height:101px}
.person{position:absolute;font-size:9px;font-weight:700;color:var(--ink)}
.person span{font-weight:400;font-size:6px;color:var(--grey);margin-left:4px}

.letterhead{left:53px;top:473px;width:295px;height:379px}
.letter-body{position:absolute;left:22px;top:92px;width:230px;font-size:5px;line-height:1.7;color:#555}
.letter-body p{margin-bottom:6px}

.envelope{left:367px;top:492px;width:305px;height:175px}
.envelope-back{left:367px;top:679px;width:305px;height:144px}
.flap{position:absolute;left:0;top:0;width:305px;height:90px}

.slide{width:230px;height:185px}
.slide-welcome{left:689px;top:384px}
.slide-thanks{left:936px;top:384px;width:228px;background:var(--black)}
.slide-about{left:689px;top:583px;height:233px}
.slide-title{position:absolute;font-size:13px;line-height:1.2;color:var(--ink)}
.thanks-text{position:absolute;right:22px;bottom:70px;font-size:9px;color:#fff}
.about-bar{position:absolute;left:0;right:0;top:12px;height:22px;background:var(--red)}
.about-bar h2{position:absolute;left:24px;top:4px;font-size:11px;font-weight:400;color:#fff}
.team-photo{position:absolute;left:12px;top:60px;width:90px;height:90px;background:linear-gradient(180deg,#d9dadd,#8e9299)}
.about-copy{position:absolute;left:110px;top:60px;width:110px;font-size:4.6px;line-height:1.6;color:#555}
</style>
</head>
<body>
<main class="canvas">

<svg width="0" height="0" style="position:absolute" aria-hidden="true">
  <defs>
    <symbol id="i-phone" viewBox="0 0 12 12"><path d="M3 1h2l1 3-1.5 1a6 6 0 0 0 2.5 2.5L8 6l3 1v2a2 2 0 0 1-2 2A8 8 0 0 1 1 3a2 2 0 0 1 2-2z" fill="#e0262b"/></symbol>
    <symbol id="i-mail" viewBox="0 0 12 12"><rect x="1" y="3" width="10" height="7" fill="#e0262b"/><path d="M1 3l5 4 5-4" stroke="#fff" fill="none"/></symbol>
    <symbol id="i-web" viewBox="0 0 12 12"><circle cx="6" cy="6" r="5" fill="none" stroke="#e0262b" stroke-width="1.4"/><path d="M1 6h10M6 1c3 3 3 7 0 10M6 1c-3 3-3 7 0 10" stroke="#e0262b" fill="none"/></symbol>
    <symbol id="i-pin" viewBox="0 0 12 12"><path d="M6 1a3.5 3.5 0 0 1 3.5 3.5C9.5 7 6 11 6 11S2.5 7 2.5 4.5A3.5 3.5 0 0 1 6 1z" fill="#e0262b"/><circle cx="6" cy="4.5" r="1.2" fill="#fff"/></symbol>
  </defs>
</svg>

<!-- FOLDER, OPEN -->
<section class="piece folder-open" aria-label="Presentation folder, inside">
  <svg class="sheet" width="427" height="360" viewBox="0 0 427 360" aria-hidden="true" style="filter:drop-shadow(0 3px 4px rgba(0,0,0,.25))">
    <path d="M0 0H427V360H262L250 322H177L165 360H0Z" fill="#fff"/>
    <rect x="0" y="12" width="427" height="7" fill="#e0262b"/>
    <rect x="0" y="250" width="427" height="7" fill="#e0262b"/>
    <rect x="0" y="264" width="427" height="1" fill="#c9c9c9"/>
  </svg>
  <div class="logo md" style="left:250px;top:86px"><span class="logo-square"></span><span class="logo-name">QV Pathway</span></div>
  <div class="tagline" style="left:263px;top:106px">Information Technology Solutions</div>

  <div class="logo sm" style="left:8px;top:170px"><span class="logo-square"></span><span class="logo-name">QV Pathway</span></div>
  <div class="small" style="left:8px;top:188px">
    <div class="contact-row"><svg class="ico"><use href="#i-pin"/></svg>58 Ravel Pine Street #04-12</div>
    <div class="contact-row"><svg class="ico"><use href="#i-phone"/></svg>+65 6000 4821</div>
    <div class="contact-row"><svg class="ico"><use href="#i-mail"/></svg>darrenm.l@qvpathway-example.com</div>
  </div>

  <div class="mark xl" style="left:150px;top:160px"><span class="mark-square"></span><span class="mark-name">QV Pathway</span></div>

  <div class="web" style="left:180px;top:250px">www.qvpathway-example.com</div>
  <div class="mark md" style="left:20px;top:290px"><span class="mark-square"></span><span class="mark-name">QV</span></div>
  <div class="mark md" style="left:360px;top:290px"><span class="mark-square"></span><span class="mark-name">QV</span></div>
</section>

<!-- FOLDER, BACK -->
<section class="piece folder-back" aria-label="Presentation folder, back">
  <div class="band" style="top:12px;height:7px"></div>
  <div class="mark lg" style="left:14px;top:150px"><span class="mark-square"></span><span class="mark-name">QV Pathway</span></div>
  <div class="band" style="top:250px;height:7px"></div>
  <div class="hairline" style="top:264px"></div>
  <div class="web" style="left:62px;top:250px">www.qvpathway-example.com</div>
</section>

<!-- BUSINESS CARD, FRONT -->
<section class="piece card card-front" aria-label="Business card, front">
  <div class="logo sm" style="left:8px;top:12px"><span class="logo-square"></span><span class="logo-name">QV Pathway</span></div>
  <div class="tagline" style="left:19px;top:27px">Information Technology Solutions</div>
  <div class="band" style="top:34px;height:3px"></div>
  <div class="person" style="left:8px;top:44px">Darren M. L.<span>Founder</span></div>
  <div class="small" style="left:8px;top:60px">
    <div class="contact-row"><svg class="ico"><use href="#i-phone"/></svg>+65 9000 3175</div>
    <div class="contact-row"><svg class="ico"><use href="#i-phone"/></svg>+65 9000 3176</div>
    <div class="contact-row"><svg class="ico"><use href="#i-mail"/></svg>darrenm.l@qvpathway-example.com</div>
  </div>
  <div class="small" style="left:8px;top:100px;font-size:4.5px">58 Ravel Pine Street #04-12 Orlan Plaza Singapore 142390</div>
  <div class="band" style="bottom:6px;height:3px"></div>
</section>

<!-- BUSINESS CARD, BACK -->
<section class="piece card card-back" aria-label="Business card, back">
  <div class="band" style="top:10px;height:3px"></div>
  <div class="mark lg" style="left:38px;top:46px"><span class="mark-square"></span><span class="mark-name">QV Pathway</span></div>
  <div class="band" style="bottom:10px;height:10px"></div>
  <div class="web" style="right:10px;bottom:11px">www.qvpathway-example.com</div>
</section>

<!-- LETTERHEAD -->
<section class="piece letterhead" aria-label="Letterhead">
  <div class="logo md" style="left:22px;top:14px"><span class="logo-square"></span><span class="logo-name">QV Pathway</span></div>
  <div class="tagline" style="left:36px;top:34px">Information Technology Solutions</div>
  <div class="band" style="top:40px;height:4px"></div>
  <div class="small" style="left:200px;top:52px;font-size:4.8px">BRN : 209874163K</div>
  <div class="letter-body">
    <p>12 March 2024<br>Mr. Alan Reyes<br>Northgate Holdings<br>Singapore</p>
    <p>Dear Mr. Reyes,</p>
    <p>Thank you for your time last week. We are pleased to share our proposal for your new systems roll-out and support plan.</p>
    <p>Our team will guide each stage, from planning to launch, and keep you updated with clear weekly reports.</p>
    <p>We look forward to working together.</p>
    <p>Yours sincerely,<br>Darren M. L.<br>Founder</p>
  </div>
  <div class="small" style="left:22px;top:318px;font-size:4.6px">
    58 Ravel Pine Street #04-12 Orlan Plaza<br>Singapore 142390<br>www.qvpathway-example.com
  </div>
  <div class="mark lg" style="left:150px;top:318px"><span class="mark-square"></span><span class="mark-name">QV Path</span></div>
  <div class="band" style="bottom:10px;height:5px"></div>
</section>

<!-- ENVELOPE, FRONT -->
<section class="piece envelope" aria-label="Envelope, front">
  <div class="logo sm" style="left:12px;top:12px"><span class="logo-square"></span><span class="logo-name">QV Pathway</span></div>
  <div class="band" style="top:28px;height:3px"></div>
  <div class="small" style="left:140px;top:66px;font-size:4.6px">58 Ravel Pine Street #04-12<br>Orlan Plaza Singapore 142390</div>
  <div class="mark lg" style="left:175px;top:90px"><span class="mark-square"></span><span class="mark-name">QV Path</span></div>
  <div class="band" style="bottom:10px;height:8px"></div>
  <div class="web" style="right:10px;bottom:10px">www.qvpathway-example.com</div>
</section>

<!-- ENVELOPE, BACK -->
<section class="piece envelope-back" aria-label="Envelope, back">
  <svg class="flap" viewBox="0 0 305 90" aria-hidden="true"><path d="M0 0H305V20L170 82Q152 90 135 82L0 20Z" fill="#111"/></svg>
  <div class="logo sm on-dark" style="left:118px;top:30px"><span class="logo-square"></span><span class="logo-name">QV Path</span></div>
</section>

<!-- SLIDE, WELCOME -->
<section class="piece slide slide-welcome" aria-label="Presentation slide, welcome">
  <div class="logo sm" style="left:12px;top:14px"><span class="logo-square"></span><span class="logo-name">QV Pathway</span></div>
  <div class="band" style="top:30px;height:3px"></div>
  <div class="slide-title" style="left:12px;top:58px">Welcome to<br>my presentation</div>
  <div class="small" style="left:12px;top:100px;font-size:4.6px;color:var(--grey)">Please insert your subtitle here</div>
  <div class="mark lg" style="left:120px;top:110px"><span class="mark-square"></span><span class="mark-name">QV Path</span></div>
  <div class="band" style="bottom:12px;height:8px"></div>
</section>

<!-- SLIDE, THANK YOU -->
<section class="piece slide slide-thanks" aria-label="Presentation slide, thank you">
  <div class="logo md on-dark" style="left:22px;top:48px"><span class="logo-square"></span><span class="logo-name">QV Pathway</span></div>
  <div class="band" style="top:70px;height:3px;left:22px;right:22px"></div>
  <div class="thanks-text">Thank You</div>
</section>

<!-- SLIDE, ABOUT US -->
<section class="piece slide slide-about" aria-label="Presentation slide, about us">
  <div class="about-bar"><h2>About Us</h2></div>
  <div class="team-photo" role="img" aria-label="Photo of the company team standing together"></div>
  <div class="about-copy">
    We help growing firms plan, build and run the systems they rely on every day. Our small team brings years of hands-on work in networks, cloud and software support, with clear advice and steady service.
  </div>
  <div class="mark md" style="left:130px;top:175px"><span class="mark-square"></span><span class="mark-name">QV Path</span></div>
  <div class="band" style="bottom:12px;height:8px"></div>
</section>

<!-- BUSINESS CARD, ALTERNATE -->
<section class="piece card-mini" aria-label="Business card, alternate">
  <div class="logo sm" style="left:8px;top:8px"><span class="logo-square"></span><span class="logo-name">QV Pathway</span></div>
  <div class="band" style="top:24px;height:3px"></div>
  <div class="person" style="left:8px;top:32px;font-size:8px">Darren M. L.<span>Founder</span></div>
  <div class="small" style="left:8px;top:48px;font-size:4.6px">
    <div class="contact-row"><svg class="ico"><use href="#i-phone"/></svg>+65 9000 3175</div>
    <div class="contact-row"><svg class="ico"><use href="#i-mail"/></svg>darrenm.l@qvpathway-example.com</div>
    <div class="contact-row"><svg class="ico"><use href="#i-web"/></svg>www.qvpathway-example.com</div>
  </div>
  <div class="mark md" style="left:150px;top:50px"><span class="mark-square"></span><span class="mark-name">QV</span></div>
  <div class="band" style="bottom:6px;height:3px"></div>
</section>

</main>
</body>
</html>
```